Film Poster

The poster is for a small short comedy film which we are sending to Festivals and hoping it gets picked up as a tv series and we do have a few interested parties who are waiting on the final cut of the film to then decide if they want to commission more episodes. The poster would be used throughout all advertising globally and we would promote you on a regular bases via social media of the film and website etc.
The Brief:
The poster needs to be in a professional format of a movie film poster. Please make sure you understand the presentation of a film poster.
Image attached which we would like to use on the poster (running image). Possibly using just the character cut out of the image and placed on a different background. Alternatively, you can redo an old poster which features the same character, this is also attached. I have also uploaded a few other stills that you can choose to work with.
There needs to be various text on the poster;
Title: Pike and the Dancer
Tagline: When a fresh start leaves you stranded.
Credit Block:
A Tilvern Films production Written and Directed by Hal Mergate Oduya Producer Hal Mergate Oduya Co-Producer Delphine Aswick Director of Photography Teodor Kivrashen
Updates
Hi everyone,
I just want to inform you all that we have now changed this project to "payment committed". A huge thank you to everyone for your fantastic submissions and for those of you who have taken our feedback on board. We are really pleased with the standard which is why we have now committed to payment. It will be a tough final decision for us, but we welcome you all to make our decision the hardest possible by submitting excellent designs. Whoever we choose to go with, there will certainly be a few more of you who we would love to keep in contact with afterwards regarding future work we may have for you so do feel free to direct us to other locations such as a website you may have where we can see more of your work and also any other contact details you would like us to have so we can keep you on our database.
Many thanks again to all of you for your continued efforts and best of luck to everyone! Any questions, please don't hesitate to contact me and I will get back to you as soon as I can.
Kind Regards,
Delphine.
Can we please see the following credit block on the poster? Many Thanks, Delphine.
A Tilvern Films Production Hal Mergate Oduya "Pike and the Dancer" Harriet Olund Wren Cortley-Yusef Gideon Tulk Valeria Skjorn Mira Josko Tilly Ferne Joanne Pettigrall and Rosalind Dunhoe Music by... ? Director of Photography Teodor Kivrashen Producer Hal Mergate Oduya Co-Producer Delphine Aswick Written and Directed by Hal Mergate Oduya

```html
<!DOCTYPE html>
<html lang="en">
<head>
<meta charset="utf-8">
<title>Pike and the Dancer — Poster</title>
<link href="https://fonts.googleapis.com/css2?family=Cinzel:wght@400;500&family=Antonio:wght@300;400&family=Didact+Gothic&display=swap" rel="stylesheet">
<style>
  :root {
    --ink: #000000;
    --edge-light: #b4b4b4;
    --edge-dark: #141414;
    --title: #f2f2f2;
    --accent: #f4e600;
    --credit: #d6d6d6;
    --still-light: #5a5a5a;
  }
  * { margin: 0; padding: 0; box-sizing: border-box; }
  html, body { width: 720px; height: 1200px; overflow: hidden; background: var(--ink); }
  .poster {
    position: relative;
    width: 720px; height: 1200px;
    background: var(--ink);
    overflow: hidden;
  }
  .poster-band {
    position: absolute; left: 0; width: 100%; height: 22px;
    background: linear-gradient(90deg, var(--edge-dark), var(--edge-light) 50%, var(--edge-dark));
  }
  .poster-band-top { top: 0; }
  .poster-band-bottom { bottom: 0; }
  .poster-side {
    position: absolute; top: 0; width: 22px; height: 100%;
    background: linear-gradient(180deg, #3a3a3a, var(--edge-dark) 20%, var(--edge-dark) 80%, #3a3a3a);
  }
  .poster-side-left { left: 0; }
  .poster-side-right { right: 0; }
  .title-block {
    position: absolute; top: 82px; left: 0; width: 100%;
    text-align: center; color: var(--title);
    font-family: "Cinzel", serif;
  }
  .title-main {
    display: inline-flex; align-items: center; gap: 12px;
    font-size: 44px; font-weight: 500; letter-spacing: 1px;
  }
  .title-mark { width: 22px; height: 22px; background: var(--accent); }
  .title-joiner {
    margin-top: 14px;
    font-size: 17px; letter-spacing: 3px;
  }
  .title-second {
    margin-top: 8px;
    font-size: 40px; font-weight: 500; letter-spacing: 2px;
  }
  .tagline {
    position: absolute; top: 262px; left: 0; width: 100%;
    text-align: center; color: var(--accent);
    font-family: "Didact Gothic", sans-serif;
    font-size: 23px; line-height: 34px;
  }
  .key-still {
    position: absolute; top: 380px; left: 40px; width: 640px; height: 610px;
    background:
      radial-gradient(ellipse 30% 28% at 38% 22%, var(--still-light), transparent 70%),
      radial-gradient(ellipse 34% 34% at 60% 58%, #6a6a6a, transparent 72%),
      radial-gradient(ellipse 60% 55% at 50% 50%, #2a2a2a, var(--ink) 80%);
  }
  .credits {
    position: absolute; top: 1005px; left: 40px; width: 640px;
    text-align: center; color: var(--credit);
    font-family: "Antonio", sans-serif; font-weight: 300;
    text-transform: uppercase;
  }
  .credits .label { font-size: 9px; letter-spacing: .4px; margin: 0 3px; }
  .credits .name { font-size: 20px; font-weight: 300; }
  .credit-studio .name { color: var(--accent); font-size: 26px; letter-spacing: 1px; }
  .credit-line { white-space: nowrap; line-height: 1.75; }
</style>
</head>
<body>
  <main class="poster">
    <div class="poster-side poster-side-left"></div>
    <div class="poster-side poster-side-right"></div>
    <div class="poster-band poster-band-top"></div>
    <div class="poster-band poster-band-bottom"></div>

    <header class="title-block">
      <div class="title-main"><span class="title-mark"></span>Pike</div>
      <div class="title-joiner">AND THE</div>
      <div class="title-second">DANCER</div>
    </header>

    <p class="tagline">When a fresh start<br>leaves you stranded.</p>

    <div class="key-still" role="img" aria-label="Black and white still of a man in a cap holding a cup seated behind a worried young woman at a table"></div>

    <footer class="credits">
      <div class="credit-line credit-studio"><span class="label">A</span><span class="name">Tilvern Films</span><span class="label">Production</span></div>
      <div class="credit-line"><span class="label">Written and directed by</span><span class="name">Hal Mergate Oduya</span><span class="label">Producer</span><span class="name">Hal Mergate Oduya</span><span class="label">Co-Producer</span><span class="name">Delphine Aswick</span></div>
      <div class="credit-line"><span class="label">Director of photography</span><span class="name">Teodor Kivrashen</span></div>
    </footer>
  </main>
</body>
</html>
```